Hollybrook Hounds Jamboree Sponsor & Stallholder Leaflet Design

Hollybrook Hounds Jamboree is the updated and refreshed version of the Pemberly Canine Fete (See www.pemberlycaninefete.co.uk).
Under new management, we need a leaflet designed to promote the event to potential stallholders and sponsors.
Hollybrook Hounds Jamboree is a fun day out for dogs and their human companions, with a range of activities for both.
As this is an outdoor event, we would like this theme in the leaflet.
It is being held in the grounds of Thistlecombe Grange - http://www.thistlecombegrange.com
Note:
Leaflet format of DL/6 page is preferred, but will accept A5/4page
I will require the final work in InDesign format
Target Market(s)
Dog owners and lovers
Industry/Entity Type
Event
Look and feel
Each slider illustrates characteristics of the customer's brand and the style your logo design should communicate.

```html
<!DOCTYPE html>
<html lang="en">
<head>
<meta charset="utf-8">
<title>Hollybrook Hounds Jamboree – Sponsor &amp; Stallholder Leaflet</title>
<link href="https://fonts.googleapis.com/css2?family=Alfa+Slab+One&family=Arimo:wght@400;700&family=Tinos:wght@400;700&display=swap" rel="stylesheet">
<style>
:root{
  --paper:#ffffff;
  --panel:#dcdddf;
  --frame:#c4c5c8;
  --inside:#c7cbd5;
  --navy:#1f2f86;
  --blue:#4b8fc4;
  --sky:#5fa3d6;
  --yellow:#f2ee3a;
  --note:#d8eef7;
  --ink:#222;
  --grey:#9a9ca0;
}
*{margin:0;padding:0;box-sizing:border-box}
html,body{width:839px;height:1200px;overflow:hidden;background:var(--paper)}
body{position:relative;font-family:"Tinos",serif;color:var(--ink)}
.abs{position:absolute}
.sans{font-family:"Arimo",sans-serif}

/* outside spread */
.outside{position:absolute;left:12px;top:12px;width:815px;height:586px;background:var(--panel)}
.cover-frame{position:absolute;left:548px;top:12px;width:279px;height:586px;border:8px solid var(--frame);background:var(--panel)}
.bracket{position:absolute;border:7px solid var(--blue);border-top-width:0;border-bottom-width:0}
.bracket::before,.bracket::after{content:"";position:absolute;top:0;bottom:0;width:10px;border-top:7px solid var(--blue);border-bottom:7px solid var(--blue)}
.bracket::before{left:-7px}.bracket::after{right:-7px}
.bracket.navy{border-color:var(--navy)}
.bracket.navy::before,.bracket.navy::after{border-color:var(--navy)}

.book{left:30px;top:88px;width:238px;height:108px;padding:18px 16px}
.book h3{font-family:"Arimo",sans-serif;font-weight:700;font-size:10.5px;color:var(--navy);line-height:14px;text-shadow:1px 1px 0 var(--yellow)}
.book p{font-family:"Arimo",sans-serif;font-size:10px;color:#333;line-height:14px}
.book .lines{margin-top:12px}
.organiser{left:20px;top:400px;width:258px;text-align:center}
.organiser h4{font-family:"Tinos",serif;font-size:11.5px;color:var(--navy);font-weight:700}
.organiser ul{list-style:none;margin-top:18px;font-size:11px;line-height:20px;color:#333}
.organiser li::before{content:"";display:inline-block;width:6px;height:6px;border-radius:50%;background:var(--grey);margin-right:6px}

/* form */
.form{left:285px;top:20px;width:262px}
.form-title{display:inline-block;font-family:"Alfa Slab One",serif;font-size:12px;color:var(--navy);background:var(--yellow);padding:2px 8px;border-left:5px solid var(--navy);border-right:5px solid var(--navy)}
.form h5{font-family:"Alfa Slab One",serif;font-size:8px;font-weight:400;color:var(--blue);margin:14px 0 4px;letter-spacing:.3px}
.form h5 .note{font-family:"Arimo",sans-serif;font-size:6px;color:var(--navy);margin-left:8px}
.paw{display:inline-block;width:9px;height:9px;border-radius:50%;background:var(--blue);margin-right:5px;vertical-align:-1px}
.form table{width:230px;border-collapse:collapse;margin-left:12px;font-family:"Arimo",sans-serif;font-size:4.6px;color:#333}
.form td{border:0.6px solid #444;padding:0 2px;height:7px;text-align:center}
.form td:first-child{text-align:left}
.form .sub{font-family:"Arimo",sans-serif;font-size:6.5px;color:var(--blue);margin:4px 0 2px 0}
.form .fine{font-family:"Arimo",sans-serif;font-size:5.2px;color:var(--navy);line-height:7px;margin-left:12px}
.return{left:286px;top:543px;width:254px;border-left:4px solid var(--navy);border-right:4px solid var(--navy);padding:3px 7px}
.return b{display:block;font-family:"Arimo",sans-serif;font-size:8px;color:var(--blue)}
.return p{font-family:"Arimo",sans-serif;font-weight:700;font-size:8px;line-height:10px;color:#111}

/* cover */
.brand{left:560px;top:112px;width:255px;text-align:center;font-family:"Alfa Slab One",serif;font-size:29px;line-height:40px;color:var(--blue);text-shadow:3px 3px 0 var(--navy)}
.dates{left:590px;top:300px;width:206px;height:84px;text-align:center;padding-top:8px;font-family:"Alfa Slab One",serif;font-size:24px;line-height:31px;color:var(--sky);text-shadow:2px 2px 0 var(--navy)}
.dates .y{color:var(--yellow)}
.cover-sub{left:560px;top:430px;width:255px;text-align:center;font-family:"Alfa Slab One",serif;font-size:15px;line-height:22px;color:var(--navy)}

/* inside spread */
.inside{position:absolute;left:12px;top:606px;width:815px;height:588px;background:var(--inside)}
.strip{position:absolute;left:12px;top:608px;width:815px;height:9px;border-top:2px solid var(--navy);font-family:"Arimo",sans-serif;font-size:4.2px;color:var(--navy);display:flex;justify-content:space-around;align-items:center}
.head{font-family:"Alfa Slab One",serif;font-weight:400;color:var(--sky);text-shadow:1.5px 1.5px 0 var(--navy);letter-spacing:.3px;white-space:nowrap}
.body{font-size:7.3px;line-height:9.3px;color:#222}
.ph{position:absolute}
.intro{left:52px;top:622px;width:230px;height:82px;border-left:4px solid var(--navy);border-top:4px solid var(--navy);padding:3px 5px;text-align:justify;font-size:6px;line-height:7.3px;overflow:hidden}
.dropcap{float:left;font-size:16px;line-height:14px;padding:1px 3px 0 0;color:var(--navy)}
.footfall{left:30px;top:708px;width:250px;text-align:center;font-family:"Arimo",sans-serif;font-size:8px;color:var(--navy);line-height:10px}
.hilite{background:var(--yellow);border:1px solid #333;padding:0 1px}
.bullets{list-style:none;font-family:"Arimo",sans-serif;font-size:8px;color:#333;line-height:17.5px;white-space:nowrap}
.bullets li::before{content:"";display:inline-block;width:9px;height:9px;border-radius:50%;background:var(--navy);margin-right:6px;vertical-align:-1px}
.promo{left:50px;top:993px}
.promo .icon{position:absolute;width:24px;height:24px;border-radius:50%;background:var(--navy)}
.promo ul{position:absolute;left:70px;top:0;list-style:none;font-family:"Arimo",sans-serif;font-size:7.2px;line-height:15px;width:170px;color:#222}
.spon-h{font-family:"Tinos",serif;font-size:10px;color:#111;border-bottom:1.5px solid #111;display:inline-block;line-height:12px}
.spon-l{font-family:"Tinos",serif;font-size:7.2px;line-height:12.2px;color:#222;text-align:center}
.pill{position:absolute;background:var(--sky);border-radius:10px;text-align:center;font-family:"Alfa Slab One",serif;font-size:11px;line-height:20px;color:var(--navy)}
.price{font-family:"Arimo",sans-serif;font-size:9px;line-height:11px;color:var(--navy);white-space:pre}
.notes{left:568px;top:871px;width:259px;background:var(--note);padding:2px 4px;font-family:"Arimo",sans-serif;font-size:5.4px;line-height:6.8px;color:var(--navy)}
.guide td{font-family:"Tinos",serif;font-size:7px;padding:0 12px 0 0;line-height:9px}
.banners{left:578px;top:1108px;width:230px;height:68px;border:1px solid var(--navy);border-left:5px solid var(--navy);border-right:5px solid var(--navy)}
.banners h6{background:var(--navy);color:var(--yellow);font-family:"Arimo",sans-serif;font-weight:400;font-size:10px;text-align:center;line-height:20px;border-bottom:3px solid var(--sky)}
.banners p{font-family:"Tinos",serif;font-size:7.4px;margin:10px 0 0 6px}
</style>
</head>
<body>

<!-- outside -->
<div class="outside"></div>
<div class="cover-frame"></div>

<div class="abs bracket book">
  <h3>To book or for more information contact the Hollybrook Hounds Jamboree team</h3>
  <div class="lines">
    <p>Call: 01632 960418</p>
    <p>Email: hello@hollybrookhounds.co.uk</p>
    <p>Website: www.hollybrookhounds.co.uk</p>
  </div>
</div>

<div class="abs organiser">
  <h4>This event is organised &amp; managed by</h4>
  <ul>
    <li>Kestrel Events Ltd</li>
    <li>9 Larchmere Lane</li>
    <li>Upper Wendham</li>
    <li>Brackford</li>
    <li>ZZ9 4QX</li>
  </ul>
</div>

<section class="abs form">
  <span class="form-title">Hollybrook Hounds Jamboree 2013</span>
  <h5><span class="paw"></span>EXHIBITOR SPACE APPLICATION FORM</h5>
  <table>
    <tr><td style="width:70px">Business Name</td><td></td></tr>
    <tr><td>Business Address</td><td></td></tr>
    <tr><td></td><td></td></tr><tr><td></td><td></td></tr>
    <tr><td>Postcode</td><td></td></tr>
    <tr><td>Business Website</td><td></td></tr>
    <tr><td>Contact Name</td><td></td></tr>
  </table>
  <h5><span class="paw"></span>SPACE REQUIRED <span class="note">*Note - All Prices Exclude VAT</span></h5>
  <p class="sub">Outside</p>
  <table>
    <tr><td>Space</td><td>Price</td><td></td><td>Total</td></tr>
    <tr><td>3m(w) x 6m(d)</td><td>@ £150</td><td></td><td></td></tr>
    <tr><td>6m(w) x 10m(d)</td><td>@ £250</td><td></td><td></td></tr>
    <tr><td>9m(w) x 10m(d)</td><td>@ £350</td><td></td><td></td></tr>
    <tr><td>12m(w) x 10m(d)</td><td>@ £450</td><td></td><td></td></tr>
  </table>
  <p class="sub">Inside</p>
  <table>
    <tr><td>Space</td><td>Price</td><td>Quantity</td><td>Total</td></tr>
    <tr><td style="height:13px">Marquee Space Minimum 6m²</td><td>@ £15/m²</td><td></td><td></td></tr>
    <tr><td style="height:13px">Power Per 13amp Socket</td><td>@ £30 each</td><td></td><td></td></tr>
    <tr><td>Table (6' x 2'6")</td><td>@ £10 each</td><td></td><td></td></tr>
  </table>
  <h5><span class="paw"></span>SHOW GUIDE ADVERT</h5>
  <table>
    <tr><td>Space</td><td>Price</td><td>Quantity</td><td>Total</td></tr>
    <tr><td>Back cover - 148w x210h</td><td>£350</td><td></td><td></td></tr>
    <tr><td>Full page - 148w x 210h</td><td>£250</td><td></td><td></td></tr>
    <tr><td>Half Page - 148w x 105h</td><td>£135</td><td></td><td></td></tr>
    <tr><td>Quarter Page - 74w x 105h</td><td>£75</td><td></td><td></td></tr>
    <tr><td>Sixth Page - 74w x 70h</td><td>£50</td><td></td><td></td></tr>
    <tr><td>Voucher Booklet</td><td>£50</td><td></td><td></td></tr>
  </table>
  <table style="margin-top:5px">
    <tr><td>Banners (60cm high)</td><td>@ £10 per mtr</td><td></td><td></td></tr>
  </table>
  <p class="fine" style="color:var(--blue)">In Competition Rings - design &amp; print not included</p>
  <table style="margin-top:8px">
    <tr><td style="width:120px">Sub Total</td><td></td></tr>
    <tr><td>VAT @ 20%</td><td></td></tr>
    <tr><td>Grand Total</td><td></td></tr>
    <tr><td>Deposit</td><td style="text-align:right">£50</td></tr>
    <tr><td>Outstanding</td><td></td></tr>
  </table>
  <p class="fine" style="margin-top:9px">*To secure the booking this form must be fully completed and signed AND accompanied by the deposit and a post dated cheque (made payable to Kestrel Events Ltd) for the outstanding balance dated one month prior to the show</p>
  <p class="fine">*If you are paying by debit/credit card, we will call you to take the deposit payment.</p>
  <p class="fine">*Bookings are subject to terms &amp; conditions and booking the event confirms that you accept these conditions.</p>
</section>

<div class="abs return">
  <b>PLEASE RETURN COMPLETED FORM TO:</b>
  <p>Hollybrook Hounds Jamboree, Kestrel Events Ltd, 9 Larchmere Lane, Upper Wendham, Brackford ZZ9 4QX</p>
</div>

<div class="abs brand">HOLLYBROOK<br>HOUNDS<br>JAMBOREE</div>
<div class="abs bracket navy dates">27 &amp; 28TH<br><span class="y">JULY, 2013</span></div>
<div class="abs cover-sub">Sponsorship &amp; Trade<br>Exhibitor Opportunities</div>

<!-- inside -->
<div class="inside"></div>
<div class="strip"><span>Hollybrook Hounds Jamboree | July 27-28, 2013 | Thistlecombe Grange, Wendham, Norfolk, UK</span><span>Hollybrook Hounds Jamboree | July 27-28, 2013 | Thistlecombe Grange, Wendham, Norfolk, UK</span><span>Hollybrook Hounds Jamboree | July 27-28, 2013 | Thistlecombe Grange, Wendham, Norfolk, UK</span></div>

<!-- column one -->
<div class="ph" role="img" aria-label="Silhouette of a sitting dog" style="left:16px;top:650px;width:30px;height:48px;background:var(--navy);border-radius:40% 40% 10% 10%"></div>
<div class="abs intro"><span class="dropcap">N</span>Pemberly Canine Fete was created and launched in 2009, in aid of Homeward Heroes, co-inciding with the deployment of the Fenland Rangers on active service to Afghanistan. Parents left behind during their deployment where amongst the committed volunteers who participated and helped in the organisation of the event. The event captured the animal loving spirit of Norfolk at a point when the whole county was passionate in their support of 'our blokes doing their bit' in Afghanistan. Expecting a few hundred dogs and 5,000 humans, it actual attracted circa 1,000 dogs, with almost 15,000 guests, the inaugural event was seen as an outstanding success. 2010 saw a visitor increase of circa 20%.</div>
<p class="abs footfall">Due to the overwhelming footfall, 2013 will become a two day event and is now known as 'HOLLYBROOK HOUNDS JAMBOREE'.</p>

<h2 class="abs head" style="left:26px;top:744px;font-size:15px">Where Is It Held?</h2>
<p class="abs body" style="left:26px;top:770px;width:255px;text-align:justify"><span class="hilite">[THISTLECOMBE GRANGE]</span> is one of Norfolk's <b>most romantic</b> and <b>impressive</b> large Edwardian country houses set in sweeping parkland. It was built to a grand design by Arthur Belmont Crane, grandson of Samuel Crane, the inventor of modern holiday travel, and is lived in today by his descendants. Although a private family home, and not open to the public, <u>Thistlecombe Grange offers a unique and magical venue for the Pemberly Canine Fete.</u></p>
<p class="abs body" style="left:26px;top:837px;width:255px"><span class="paw" style="background:var(--navy)"></span>Near Marlow Heath, in North Norfolk, Thistlecombe Grange is approximately 30 minutes from Eastbridge.</p>

<h2 class="abs head" style="left:26px;top:874px;font-size:15px">Who Will Attend?</h2>
<div class="ph" role="img" aria-label="Silhouettes of two standing dogs" style="left:194px;top:864px;width:72px;height:32px;background:linear-gradient(90deg,var(--navy) 0 45%,transparent 45% 55%,var(--navy) 55%);border-radius:6px"></div>
<p class="abs body" style="left:26px;top:902px;width:255px;text-align:justify">The target audience for this event is anyone who likes, owns or has an interest in dogs! Heavily promoted to dog lovers and owners, across several mediums, it attracts visitors of all ages across the demographic spectrum.</p>

<h2 class="abs head" style="left:26px;top:958px;font-size:15px">How Will It Be Promoted?</h2>
<div class="abs promo">
  <span class="icon" style="left:0;top:0"></span><span class="icon" style="left:32px;top:0"></span>
  <span class="icon" style="left:0;top:36px"></span><span class="icon" style="left:32px;top:36px"></span>
  <span class="icon" style="left:0;top:72px"></span><span class="icon" style="left:32px;top:72px"></span>
  <ul>
    <li>Dedicated website</li>
    <li>Social Media - Chatterbox, Pinwheel etc</li>
    <li>Regional Advertising</li>
    <li>Dog &amp; pet Press</li>
    <li>Regional Radio</li>
    <li>Regional database via email</li>
  </ul>
</div>
<p class="abs sans" style="left:26px;top:1108px;font-size:5.5px">Thistlecombe Grange</p>
<div class="ph" role="img" aria-label="Black and white photograph of Thistlecombe Grange house and parkland trees" style="left:12px;top:1118px;width:270px;height:76px;background:linear-gradient(180deg,#e9e9e9 0%,#bdbdbd 35%,#4a4a4a 65%,#2a2a2a 100%)"></div>

<!-- column two -->
<h2 class="abs head" style="left:296px;top:634px;font-size:17px">WHY SPONSOR?</h2>
<ul class="abs bullets" style="left:294px;top:666px">
  <li>Give your brands or products exposure to circa 20,000 visitors</li>
  <li>Access a highly targeted mar</li>
  <li>Lead generation</li>
  <li>Brand positioning</li>
  <li>Increase brand recognition</li>
</ul>
<div class="ph" role="img" aria-label="Silhouette of a family of four walking a dog" style="left:440px;top:702px;width:104px;height:44px;background:var(--navy);opacity:.85;border-radius:16px 16px 4px 4px"></div>

<h2 class="abs head" style="left:296px;top:770px;font-size:17px;line-height:22px">WHAT DOES SPONSORSHIP<br>GIVE YOU?</h2>
<p class="abs sans" style="left:330px;top:822px;width:220px;font-size:7.4px;font-weight:700;color:#333;line-height:10px"><span style="color:var(--yellow);font-size:14px;position:absolute;left:-18px;top:-2px">★</span><span style="background:var(--yellow)">There are four types of sponsorship, dependant of your badget and marketing goals.</span></p>

<div class="abs" style="left:294px;top:856px;width:128px">
  <span class="spon-h">MAIN EVENT SPONSOR</span>
  <p class="spon-l" style="text-align:left">*Branding on all media communications: leaflets, tickets, website, emails etc</p>
  <p class="spon-l">*Large Exhibition Space<br>*Sign and Banner Rights across the event venue and rings<br>(banner productionincluded)<br>*Local, regional and national Media Exposure<br>*2 pages in the show guide<br>*Global Judging rights<br>*Massive Consumer Awareness<br>*20 Complimentary tickets</p>
</div>
<div class="ph" role="img" aria-label="Silhouette of a large standing dog" style="left:440px;top:850px;width:66px;height:58px;background:var(--navy);border-radius:30% 40% 10% 10%"></div>
<div class="abs" style="left:428px;top:923px;width:122px;text-align:center">
  <span class="spon-h">RING SPONSOR</span>
  <p class="spon-l">*Exhibition Space<br>*Joint Banner Rights in the event ring<br>(banner production included)<br>*1 pages in the show guide<br>*Ring Judging rights<br>*5 Complimentary tickets</p>
</div>
<div class="abs" style="left:294px;top:1026px;width:126px;height:5px;background:var(--sky)"></div>
<div class="abs" style="left:428px;top:1030px;width:122px;height:5px;background:var(--yellow)"></div>
<div class="abs" style="left:294px;top:1036px;width:126px;text-align:center">
  <span class="spon-h">GIFT/SAMPLE SPONSOR</span>
  <p class="spon-l">*Promote your brand or product by supplying gift or sample<br>*Data collection opportunity<br>*Exhibition Space<br>*1/2 page in the show guide</p>
</div>
<div class="abs" style="left:428px;top:1038px;width:122px;text-align:center">
  <span class="spon-h">COMPETITION SPONSOR</span>
  <p class="spon-l">*Exhibition Space<br>*1/2 page in the show guide<br>*Competition Judging rights<br>*2 Complimentary tickets</p>
</div>
<div class="abs bracket" style="left:298px;top:1140px;width:252px;height:36px;text-align:center"><span class="head" style="font-size:20px;line-height:36px">SPONSORSHIP</span></div>

<!-- column three -->
<div class="abs bracket navy" style="left:590px;top:628px;width:226px;height:28px;text-align:center"><span class="head" style="font-size:16px;line-height:28px">TRADE EXHIBITORS</span></div>
<p class="abs sans" style="left:592px;top:661px;width:230px;color:var(--navy);font-size:7px;line-height:9px">There are several space options available to exhibitors, both covered and grass space only. Covering the two days of the event, exhibitors also get a line listing in the event show guide and website.</p>
<div class="pill" style="left:596px;top:700px;width:130px">Grass Space Only</div>
<div class="ph" role="img" aria-label="Grass tuft icon in a yellow circle" style="left:568px;top:726px;width:52px;height:52px;border-radius:50%;background:var(--yellow)"></div>
<div class="abs price" style="left:652px;top:726px">3m(w) x 6m(d) --------- £150
6m(w) x 10m(d) -------- £250
9m(w) x 10m(d) -------- £350
12m(w) x 10m(d) ------- £450</div>
<div class="pill" style="left:572px;top:780px;width:235px">Marquee Space</div>
<div class="ph" role="img" aria-label="Marquee tent icon in a yellow circle" style="left:768px;top:812px;width:56px;height:56px;border-radius:50%;background:var(--yellow)"></div>
<p class="abs sans" style="left:600px;top:806px;width:150px;text-align:center;font-size:10px;color:var(--navy);line-height:12px">£15 per square meter<br><span style="font-size:8.5px">(minimum 6 square meters)</span></p>
<p class="abs sans" style="left:568px;top:838px;font-size:7.4px;line-height:13px;color:#222">Power (Marquee Only) - £30 per 13amp Socket<br>Table (6' x 2'6") ----------------------------- £10 each</p>
<div class="abs notes"><b>NOTES:</b><br>*All exhibitors must have valid and suitable public, product &amp; employee liability insurance<br>*All (human) food based exhibitors must have suitable food hygiene qualifications and certification</div>
<h3 class="abs head" style="left:572px;top:910px;font-size:12px">Additional Marketing Opportunities</h3>
<div class="ph" role="img" aria-label="Cover of the event show guide" style="left:568px;top:934px;width:30px;height:40px;background:var(--navy)"></div>
<div class="abs" style="left:604px;top:934px;width:222px">
  <span class="spon-h" style="border:none">SHOW GUIDE</span>
  <p class="body" style="font-size:6.6px;line-height:8.2px">A minimum of 32 pages, the show guide not only contains useful features and stories, but also a full listing of all sponsors and exhibitors.</p>
  <table class="guide">
    <tr><td></td><td>Exhibitor</td><td>Standard Advertiser</td></tr>
    <tr><td>Back Cover</td><td>£350</td><td>£700</td></tr>
    <tr><td>Full Page</td><td>£250</td><td>£500</td></tr>
    <tr><td>Half Page</td><td>£135</td><td>£270</td></tr>
    <tr><td>Quarter Page</td><td>£75</td><td>£150</td></tr>
    <tr><td>Sixth Page</td><td>£75</td><td>£150</td></tr>
  </table>
</div>
<div class="ph" role="img" aria-label="Pair of discount vouchers" style="left:784px;top:1010px;width:38px;height:34px;background:var(--yellow);transform:rotate(-20deg)"></div>
<div class="abs" style="left:568px;top:1044px;width:206px;text-align:center"><span class="spon-h">PROMOTIONAL VOUCHER</span></div>
<p class="abs body" style="left:568px;top:1062px;width:226px;font-size:6.7px;line-height:8.3px;text-align:justify">The centre of the guide will contain a pull out voucher booklet, with 6 vouchers per page. Exhibitors offering a special promotion, price or service during the event can promote it via a voucher, which will not only highlight the offer, but also identify the location of their stand. This costs £50 per voucher</p>
<div class="abs banners"><h6>BANNERS IN COMPETITION RINGS</h6><p>£10 per meter (60cm high) - design &amp; production not included</p></div>

</body>
</html>
```